Powepoint Templates From Logo

Hello,

I am looking for a template for PowerPoint presentations for a new company selling Brivonlux's. The PowerPoint should keep the look and feel of our newly designed website ( which is still under development ) http://brivonlux.com/development/

I have attached our Logo which should be included in this template.
This PowerPoint will be used towards client during demonstrations and for internal use.

This template should be complete with fonts and colors of the text for both headlines and bullets/normal text.

I guess the easiest way for me to determine what I like is to see some dummy info/text on the submitted designs.

Thanks

Industry/Entity Type

It Company

Requirements
Must have
• Should include our logo

```html
<!DOCTYPE html>
<html lang="en">
<head>
<meta charset="utf-8">
<title>Brivonlux Presentation Template</title>
<link href="https://fonts.googleapis.com/css2?family=Roboto+Condensed:wght@400;700&family=Arimo:wght@700&display=swap" rel="stylesheet">
<style>
  :root {
    --green: #6b9a00;
    --green-bright: #8cbf1a;
    --ink: #111111;
    --text: #3a3a3a;
    --muted: #7a7a7a;
    --rule: #d9d9d9;
    --white: #ffffff;
  }
  html, body {
    margin: 0;
    padding: 0;
    width: 1200px;
    height: 900px;
    overflow: hidden;
    background: var(--white);
  }
  .slide {
    position: relative;
    width: 1200px;
    height: 900px;
    overflow: hidden;
    font-family: "Roboto Condensed", "Arial Narrow", sans-serif;
    background:
      radial-gradient(ellipse 700px 260px at 720px 60px, rgba(255,255,255,0.95), rgba(255,255,255,0) 70%),
      linear-gradient(180deg, #dcdcdc 0px, #f3f3f3 140px, #f7f7f7 150px, #efefef 200px, #ffffff 330px, #ffffff 100%);
  }
  .header-rule {
    position: absolute;
    left: 0; top: 147px;
    width: 1200px; height: 2px;
    background: linear-gradient(90deg, rgba(200,200,200,0.2), #cfcfcf 40%, #d8d8d8 100%);
  }
  .slide-title {
    position: absolute;
    left: 56px; top: 52px;
    margin: 0;
    font-weight: 700;
    font-size: 58px;
    line-height: 1;
    color: var(--ink);
    letter-spacing: -0.5px;
  }
  .brand {
    position: absolute;
    left: 880px; top: 40px;
    display: flex;
    align-items: center;
    gap: 18px;
  }
  .brand-mark {
    width: 96px; height: 96px;
    border-radius: 50%;
    background: var(--green-bright);
  }
  .brand-name {
    font-weight: 700;
    font-size: 46px;
    color: #8a8a8a;
  }
  .content-title {
    position: absolute;
    left: 50px; top: 218px;
    margin: 0;
    font-family: "Arimo", Arial, sans-serif;
    font-weight: 700;
    font-size: 42px;
    color: var(--green);
  }
  .subtext {
    position: absolute;
    left: 52px; top: 282px;
    margin: 0;
    width: 1100px;
    font-size: 25px;
    line-height: 40px;
    color: var(--text);
  }
  .data-table {
    position: absolute;
    left: 51px; top: 374px;
    width: 1096px;
    border-collapse: collapse;
    border: 2px solid var(--green);
    background: var(--white);
    table-layout: fixed;
  }
  .data-table th,
  .data-table td {
    box-sizing: border-box;
    white-space: nowrap;
    overflow: hidden;
    text-align: left;
  }
  .data-table th {
    height: 48px;
    background: var(--green);
    color: var(--white);
    font-weight: 400;
    font-size: 25px;
    padding: 0;
    border-left: 2px solid var(--white);
  }
  .data-table th:first-child { border-left: none; }
  .data-table td {
    height: 46px;
    padding: 0;
    font-size: 21px;
    color: var(--muted);
    border-bottom: 1px solid #e6e6e6;
    border-left: 1px solid var(--rule);
  }
  .data-table td:first-child { border-left: none; }
  .data-table tr:last-child td { border-bottom: 3px double #e3e3e3; }
  .col-w1 { width: 179px; }
  .col-w2 { width: 240px; }
  .col-w3 { width: 315px; }
  .col-w4 { width: 362px; }
  .data-table th.col-1 { padding-left: 34px; }
  .data-table td.col-1 { padding-left: 34px; }
  .data-table th.col-2 { padding-left: 50px; }
  .data-table td.col-2 { padding-left: 17px; }
  .data-table th.col-3 { padding-left: 95px; }
  .data-table td.col-3 { padding-left: 47px; }
  .data-table th.col-4 { padding-left: 140px; }
  .data-table td.col-4 { padding-left: 56px; }
  .footer-rule {
    position: absolute;
    left: 0; top: 817px;
    width: 1084px; height: 2px;
    background: var(--green-bright);
  }
  .page-number {
    position: absolute;
    left: 1083px; top: 784px;
    width: 62px; height: 62px;
    box-sizing: border-box;
    border: 2px solid var(--green-bright);
    border-radius: 50%;
    background: var(--white);
    display: flex;
    align-items: center;
    justify-content: center;
    font-weight: 700;
    font-size: 26px;
    color: #222;
  }
  .copyright {
    position: absolute;
    left: 46px; top: 838px;
    margin: 0;
    font-size: 24px;
    color: #555555;
  }
</style>
</head>
<body>
<main class="slide">
  <h1 class="slide-title">Persentation Title Here</h1>
  <div class="brand">
    <span class="brand-mark"></span>
    <span class="brand-name">Brivonlux</span>
  </div>
  <div class="header-rule"></div>

  <h2 class="content-title">Content Title Here</h2>
  <p class="subtext">Subtext Content Here, Subtext Content Here Subtext Content Here, Subtext Content Here<br>Subtext Content Here, Subtext Content Here Subtext Content Here,</p>

  <table class="data-table">
    <colgroup>
      <col class="col-w1">
      <col class="col-w2">
      <col class="col-w3">
      <col class="col-w4">
    </colgroup>
    <thead>
      <tr>
        <th class="col-1">Title here</th>
        <th class="col-2">Title here</th>
        <th class="col-3">Title here</th>
        <th class="col-4">Title here</th>
      </tr>
    </thead>
    <tbody>
      <tr><td class="col-1">Sub Text here</td><td class="col-2">Sub Text here</td><td class="col-3">Sub Text here</td><td class="col-4">Sub Text here</td></tr>
      <tr><td class="col-1">Sub Text here</td><td class="col-2">Sub Text here</td><td class="col-3">Sub Text here</td><td class="col-4">Sub Text here</td></tr>
      <tr><td class="col-1">Sub Text here</td><td class="col-2">Sub Text here</td><td class="col-3">Sub Text here</td><td class="col-4">Sub Text here</td></tr>
      <tr><td class="col-1">Sub Text here</td><td class="col-2">Sub Text here</td><td class="col-3">Sub Text here</td><td class="col-4">Sub Text here</td></tr>
      <tr><td class="col-1">Sub Text here</td><td class="col-2">Sub Text here</td><td class="col-3">Sub Text here</td><td class="col-4">Sub Text here</td></tr>
      <tr><td class="col-1">Sub Text here</td><td class="col-2">Sub Text here</td><td class="col-3">Sub Text here</td><td class="col-4">Sub Text here</td></tr>
      <tr><td class="col-1">Sub Text here</td><td class="col-2">Sub Text here</td><td class="col-3">Sub Text here</td><td class="col-4">Sub Text here</td></tr>
    </tbody>
  </table>

  <div class="footer-rule"></div>
  <div class="page-number">01</div>
  <p class="copyright">Copyright@Brivonlux</p>
</main>
</body>
</html>
```